Business Card Design

Electronic Security
Alarm Systems
CCTV
Electronic Access Control
Security System Integration

Industry/Entity Type

Business

Contact Information for Business Card

Gareth Linwood
PO Box 862
Yarrowdale Qld 4173
Phone 07 38265140
Mob 0428637291

```html
<!DOCTYPE html>
<html lang="en">
<head>
<meta charset="utf-8">
<title>Korva Security – Business Card</title>
<link href="https://fonts.googleapis.com/css2?family=Open+Sans:wght@400;600&display=swap" rel="stylesheet">
<style>
  :root {
    --backdrop: #5b5c5e;
    --card-dark: #2e2f33;
    --card-light: #ffffff;
    --accent-blue: #29a3dd;
    --accent-orange: #f6a623;
    --text-light: #f2f2f2;
  }
  html, body {
    margin: 0;
    width: 1200px;
    height: 1000px;
    overflow: hidden;
    background: var(--backdrop);
    font-family: "Open Sans", Arial, sans-serif;
  }
  .canvas { position: relative; width: 1200px; height: 1000px; }
  .card {
    position: absolute;
    box-shadow: 0 6px 14px rgba(0,0,0,0.35);
    overflow: hidden;
  }
  .card-front {
    left: 183px; top: 152px; width: 574px; height: 335px;
    background: var(--card-dark);
    display: flex; align-items: center; justify-content: center; gap: 14px;
  }
  .brand-square { width: 22px; height: 22px; background: var(--accent-orange); }
  .brand-name {
    font-weight: 600; font-size: 46px; letter-spacing: 4px;
    color: var(--accent-blue);
  }
  .card-back {
    left: 448px; top: 530px; width: 570px; height: 333px;
    background: var(--card-dark);
  }
  .card-back .swoosh { position: absolute; inset: 0; }
  .back-brand {
    position: absolute; left: 30px; top: 190px; width: 210px;
    display: flex; align-items: center; justify-content: center; gap: 10px;
  }
  .back-brand .brand-name { font-size: 40px; letter-spacing: 3px; }
  .back-brand .brand-square { width: 18px; height: 18px; }
  .details {
    position: absolute; right: 30px; top: 32px;
    text-align: right; color: var(--text-light);
  }
  .services { list-style: none; margin: 0; padding: 0; font-size: 14.5px; line-height: 19.7px; }
  .services li::after {
    content: ""; display: inline-block; width: 8px; height: 8px;
    background: var(--accent-orange); margin-left: 8px; vertical-align: 1px;
  }
  .person {
    margin: 28px 0 0; font-size: 17.5px; font-weight: 400;
    color: var(--accent-orange); letter-spacing: 0.3px;
  }
  .contact { margin-top: 16px; font-size: 14.5px; line-height: 24px; }
  .contact .row { display: flex; justify-content: flex-end; align-items: center; gap: 3px; }
  .contact svg { width: 16px; height: 16px; }
  .address { margin-top: 10px; font-size: 14.5px; line-height: 23px; font-style: normal; }
</style>
</head>
<body>
<div class="canvas">
  <section class="card card-front">
    <span class="brand-square"></span>
    <span class="brand-name">KORVA</span>
  </section>

  <section class="card card-back">
    <svg class="swoosh" viewBox="0 0 570 333" preserveAspectRatio="none" aria-hidden="true">
      <path d="M0,0 L250,0 Q348,175 232,333 L0,333 Z" fill="var(--accent-orange)"/>
      <path d="M0,0 L262,0 Q352,140 296,245 L0,245 Z" fill="var(--accent-blue)"/>
      <path d="M0,0 L235,0 Q325,170 210,333 L0,333 Z" fill="var(--card-light)"/>
    </svg>

    <div class="back-brand">
      <span class="brand-square"></span>
      <span class="brand-name">KORVA</span>
    </div>

    <div class="details">
      <ul class="services">
        <li>Electronic Security</li>
        <li>Alarm Systems</li>
        <li>CCTV</li>
        <li>Electronic Access Control</li>
        <li>Security System Integration</li>
      </ul>
      <p class="person">GARETH LINWOOD</p>
      <div class="contact">
        <div class="row">07 38265140
          <svg viewBox="0 0 16 16" aria-hidden="true"><path d="M4 2 L6.5 2 L7.5 5.5 L6 6.8 Q7.5 10 10 11 L11.3 9.5 L14.5 10.5 L14.5 13 Q9 14.5 5 10 Q1.5 6 4 2 Z" fill="var(--accent-blue)"/></svg>
        </div>
        <div class="row">0428637291
          <svg viewBox="0 0 16 16" aria-hidden="true"><rect x="4.5" y="1.5" width="7" height="13" rx="1.2" fill="none" stroke="var(--accent-blue)" stroke-width="1.4"/><circle cx="8" cy="12.3" r="0.8" fill="var(--accent-blue)"/></svg>
        </div>
      </div>
      <address class="address">PO Box 862<br>Yarrowdale Qld 4173</address>
    </div>
  </section>
</div>
</body>
</html>
```